Tallyleaf Web Design

Create Website Design for Tallyleaf. Tallyleaf is online application for collaboration team work system (task list management). More concept design for this project please find attach file ("tallyleaf website concept.pdf") . But my concept is just describe minimal features not bind design

For tallyleaf logo, i had already attach files. But i had not decided what color i chose, so it's okay if you suggest logo color for your suitable website design.
Updates

Dear All Designer,

I like brisk carousel (http://quorvanlabs.example/brisk-carousel/),
may be your concept design can adjust with this concept.
but don't worry about script for brisk carousel, my team will be handle
You just make website design to suitable with brisk carousel

but if you had own website design concept are welcome

thanks

Target Market(s)

Business Company

Industry/Entity Type

Management

```html
<!DOCTYPE html>
<html lang="en">
<head>
<meta charset="utf-8">
<title>Tallyleaf – Manage your tasks seamlessly</title>
<link href="https://fonts.googleapis.com/css2?family=Ubuntu:ital,wght@0,400;0,500;1,400;1,500&display=swap" rel="stylesheet">
<style>
:root{
  --sky:#1f9cc3;
  --sky-dark:#1784ab;
  --sky-light:#39b3d6;
  --navy:#1e4770;
  --navy-edge:#163656;
  --green:#5dba1b;
  --green-dark:#43960c;
  --orange:#f08a1c;
  --ink:#4a4a4a;
  --ink-blue:#1d5d93;
  --paper:#f0f0f0;
  --white:#ffffff;
  --strip:#232323;
  --foot:#2f2a27;
  --foot-text:#e9e6e2;
  --field-text:#b8b8b8;
}
*{box-sizing:border-box;margin:0;padding:0}
html,body{width:1097px;height:1200px;overflow:hidden;background:var(--paper)}
body{font-family:'Ubuntu',sans-serif;color:var(--ink);position:relative}
.page{position:relative;width:1097px;height:1200px}
.abs{position:absolute}

/* header */
.site-header{left:0;top:0;width:1097px;height:67px;background:var(--white);border-bottom:2px solid #d9eaf1}
.brand{left:150px;top:17px;display:flex;align-items:center;gap:8px;font-size:29px;color:var(--sky);font-weight:400}
.brand-dot{width:14px;height:14px;border-radius:50%;background:var(--orange)}
.btn-head{top:20px;height:28px;width:82px;border-radius:3px;font-size:12px;font-weight:500;display:flex;align-items:center;justify-content:center}
.btn-login{left:789px;background:linear-gradient(#f2f2f2,#d4d4d4);border:1px solid #b5b5b5;color:#444}
.btn-signup{left:878px;background:linear-gradient(#3fb4db,#1a8fbd);border:1px solid #137ba4;color:var(--white)}

/* hero */
.hero{left:0;top:67px;width:1097px;height:544px;background:radial-gradient(ellipse at 60% 30%,var(--sky-light),var(--sky) 55%,var(--sky-dark))}
.hero-title{left:137px;top:105px;width:360px;font-size:26px;line-height:31px;font-weight:500;color:var(--white)}
.hero-text{left:137px;top:182px;width:330px;font-size:13.2px;line-height:16.5px;color:var(--white)}
.hero-text a{color:#0d3f5e;text-decoration:none}
.field{background:var(--white);border:2px solid #d3e5ec;border-radius:3px;color:var(--field-text);font-size:13.5px;display:flex;align-items:center;padding-left:13px}
.f-email{left:137px;top:246px;width:324px;height:35px}
.f-pass{left:137px;top:294px;width:153px;height:35px}
.f-confirm{left:308px;top:294px;width:153px;height:35px}
.btn-free{left:137px;top:341px;width:324px;height:54px;border-radius:3px;background:linear-gradient(#6cc820,var(--green-dark));border:1px solid #3b8a0a;color:var(--white);font-size:19px;display:flex;align-items:center;justify-content:center}
.alt-signup{left:179px;top:415px;font-size:13px;color:#123f5c;display:flex;gap:6px;align-items:baseline}
.alt-signup b{font-size:14px;font-weight:500}
.slider-dots{left:138px;top:481px;display:flex;gap:5px}
.slider-dots span{width:13px;height:13px;border-radius:50%;background:var(--navy);border:1px solid #0f2d47}
.slider-dots span.on{background:var(--white);border-color:#c7dfe8}
.hero-art{left:446px;top:94px;width:514px;height:429px;border-radius:10px;background:radial-gradient(ellipse at 50% 60%,rgba(255,255,255,.55),rgba(255,255,255,.08) 70%)}

/* feature cards */
.feature{top:532px;width:256px;height:60px;background:var(--navy);border:1px solid var(--navy-edge);border-radius:3px;display:flex;align-items:center;gap:12px;padding-left:13px;color:var(--white);font-size:15px;font-weight:500;white-space:nowrap;box-shadow:inset 0 1px 0 rgba(255,255,255,.12)}
.feature svg{flex:none}
.fc1{left:138px}.fc2{left:420px;padding-left:8px;gap:8px}.fc3{left:703px}

/* about */
.about-card{left:137px;top:644px;width:823px;height:406px;background:var(--white);border:1px solid #dcdcdc;border-radius:4px}
.about-title{left:162px;top:676px;font-size:26px;font-weight:400;color:var(--ink)}
.about-title span{color:var(--ink-blue)}
.about-tagline{left:520px;top:679px;width:422px;text-align:right;font-size:20.5px;font-weight:400;font-style:italic;color:var(--ink-blue);white-space:nowrap}
.about-tagline em{color:var(--orange);font-style:italic}
.about-copy{left:162px;top:727px;width:375px;font-size:13px;line-height:17.1px;color:#555}
.about-copy p{margin-bottom:17.1px}
.about-art{left:588px;top:730px;width:306px;height:249px;background:radial-gradient(circle at 55% 55%,#bcd9ee 0,#e9eef2 40%,#d3d5d7 100%);box-shadow:0 18px 18px -14px rgba(0,0,0,.35)}

/* signup strip */
.signup-strip{left:0;top:1077px;width:1097px;height:39px;background:var(--strip)}
.strip-field{top:1082px;width:197px;height:29px;background:var(--white);border-radius:2px;color:var(--field-text);font-size:12px;display:flex;align-items:center;padding-left:14px}
.sf1{left:140px}.sf2{left:347px}.sf3{left:555px}
.strip-btn{left:762px;top:1082px;width:198px;height:29px;background:linear-gradient(#6cc820,var(--green-dark));border-radius:2px;color:var(--white);font-size:12.5px;display:flex;align-items:center;justify-content:center}

/* footer */
.site-footer{left:0;top:1116px;width:1097px;height:84px;background:var(--foot)}
.foot-nav{left:140px;top:1141px;display:flex;gap:0;font-size:9.5px;color:var(--foot-text)}
.foot-nav a{color:inherit;text-decoration:none;margin-right:25px}
.copyright{left:140px;top:1168px;font-size:8.5px;color:var(--foot-text)}
.follow{left:800px;top:1157px;font-size:9.5px;color:var(--foot-text)}
.social{top:1149px;width:26px;height:26px;border-radius:50%}
.s1{left:870px;background:#3a5aa0}.s2{left:902px;background:#2fb2e6}.s3{left:934px;background:#f26b1d}
</style>
</head>
<body>
<div class="page">

  <header class="abs site-header"></header>
  <div class="abs brand"><span>tallyleaf</span><span class="brand-dot"></span></div>
  <div class="abs btn-head btn-login">LOGIN</div>
  <div class="abs btn-head btn-signup">SIGN UP</div>

  <section class="abs hero"></section>
  <h1 class="abs hero-title">Manage your tasks<br>seamlessly from anywhere.</h1>
  <p class="abs hero-text">Lorem ipsum dolor sit amet consecutor. Lorem ipsum dolor sit amet consecutor. Lorem ipsum dolor sit amet consecutor. <a href="#">Learn More</a></p>
  <div class="abs field f-email">Email</div>
  <div class="abs field f-pass">Password</div>
  <div class="abs field f-confirm">Confirm password</div>
  <div class="abs btn-free">SIGN UP NOW FOR FREE</div>
  <div class="abs alt-signup">Or sign up using <b>Linkpost</b> or <b>Searchly</b></div>
  <div class="abs slider-dots"><span class="on"></span><span></span><span></span><span></span></div>
  <div class="abs hero-art" role="img" aria-label="Illustration of the task app on a desktop window and phone, with a clock, calendar, cloud sync icons and a video play button"></div>

  <div class="abs feature fc1">
    <svg width="38" height="38" viewBox="0 0 38 38" aria-hidden="true"><rect x="3" y="3" width="30" height="33" rx="2" fill="#fff"/><rect x="3" y="3" width="30" height="6" fill="#4c8cd0"/><g stroke="#9bb3c9" stroke-width="2"><line x1="8" y1="15" x2="22" y2="15"/><line x1="8" y1="21" x2="20" y2="21"/><line x1="8" y1="27" x2="18" y2="27"/></g><line x1="34" y1="14" x2="22" y2="32" stroke="#f0b429" stroke-width="4"/></svg>
    Customize Application
  </div>
  <div class="abs feature fc2">
    <svg width="64" height="44" viewBox="0 0 70 48" aria-hidden="true"><ellipse cx="34" cy="20" rx="22" ry="13" fill="#d8eefa"/><rect x="4" y="22" width="16" height="20" rx="2" fill="#c9d3db"/><rect x="56" y="24" width="11" height="20" rx="2" fill="#222"/><rect x="58" y="27" width="7" height="13" fill="#7fc3e6"/></svg>
    Synchronize All Device
  </div>
  <div class="abs feature fc3">
    <svg width="38" height="38" viewBox="0 0 38 38" aria-hidden="true"><rect x="2" y="3" width="34" height="32" fill="#fff"/><rect x="2" y="3" width="34" height="7" fill="#2c6bb3"/><g stroke="#9aa9b7" stroke-width="1"><line x1="2" y1="17" x2="36" y2="17"/><line x1="2" y1="24" x2="36" y2="24"/><line x1="2" y1="30" x2="36" y2="30"/><line x1="13" y1="10" x2="13" y2="35"/><line x1="25" y1="10" x2="25" y2="35"/></g></svg>
    Report
  </div>

  <section class="abs about-card"></section>
  <h2 class="abs about-title">About <span>Tallyleaf</span></h2>
  <h3 class="abs about-tagline">Customize Online Collaboration <em>Team</em> Work</h3>
  <div class="abs about-copy">
    <p>Lorem ipsum dolor sit amet consecutor. Lorem ipsum dolor sit amet consecutor. Lorem ipsum dolor sit amet consecutor. Lorem ipsum dolor sit amet consecutor. Lorem ipsum dolor sit amet consecutor. Lorem ipsum dolor sit amet consecutor.</p>
    <p>Lorem ipsum dolor sit amet consecutor. Lorem ipsum dolor sit amet consecutor. Lorem ipsum dolor sit amet consecutor. Lorem ipsum dolor sit amet consecutor.</p>
    <p>Lorem ipsum dolor sit amet consecutor. Lorem ipsum dolor sit amet consecutor. Lorem ipsum dolor sit amet consecutor. Lorem ipsum dolor sit amet consecutor.</p>
  </div>
  <div class="abs about-art" role="img" aria-label="Illustration of user profile cards under a magnifying glass, with a faint search field for finding users"></div>

  <div class="abs signup-strip"></div>
  <div class="abs strip-field sf1">Email</div>
  <div class="abs strip-field sf2">Password</div>
  <div class="abs strip-field sf3">Confirm password</div>
  <div class="abs strip-btn">SIGN UP NOW FOR FREE</div>

  <footer class="abs site-footer"></footer>
  <nav class="abs foot-nav"><a href="#">Home</a><a href="#">Tour</a><a href="#">Pricing</a><a href="#">Free Trial</a><a href="#">Customers</a><a href="#">About</a><a href="#">Blog</a><a href="#">Support</a><a href="#">Contact Us</a></nav>
  <div class="abs copyright">Copyright © 2013 tallyleaf. All Rights Reserved</div>
  <div class="abs follow">Follow us on :</div>
  <span class="abs social s1" aria-label="Social network"></span>
  <span class="abs social s2" aria-label="Social network"></span>
  <span class="abs social s3" aria-label="Blog"></span>

</div>
</body>
</html>
```